Womans Supplement Designs

Launching a Supplement company and need to get some initial designs created, I've attached our logo and the bottle type that I want the samples done one.

This project is for our Whey Protein we are starting with Vanilla, chocolate and strawberry banana

(ALL DESIGN VARIATIONS MUST BE A WHITE BOTTLE NOT BLACK)

(FOR DESIGN SAMPLES PLEASE USE THE SUPPLEMENT BOTTLE STYLE I PROVIDED)

Whoever is selected the winner I will have more work for you to complete the disigns for the rest of the products in the line, Just want to get this shake completed first

Target Market(s)

Women

Requirements
Must have
• Must have our current logo involved

the name of this product will be "KIVA LUM"

Must have this slogan,

ALL-IN-ONE PREMIUM PROTEIN NUTRITIONAL SHAKE FOR BLACK WOMEN

This is our meal replacement

the design should try to keep the same look and feel of the existing provided supplement images

we are starting with chocolate, vanilla and strawberry banana

this is for women and should look colorful and appeal to them
Should not have
• Do not use an image of a person or lady, don't want it branded to a person

```html
<!DOCTYPE html>
<html lang="en">
<head>
<meta charset="utf-8">
<title>Kiva Lum Whey Protein Label</title>
<link rel="stylesheet" href="https://fonts.googleapis.com/css2?family=Roboto+Condensed:wght@300;700&family=Roboto:wght@400;500;700&display=swap">
<style>
  :root {
    --page: #ffffff;
    --panel: #2b2b2d;
    --panel-light: #3a3a3c;
    --pink: #e2385f;
    --pink-soft: #ef4d72;
    --berry: #d8263a;
    --berry-light: #f05a66;
    --leaf: #5a9a3e;
    --white: #ffffff;
    --ink-soft: #dcdcdc;
  }
  * { box-sizing: border-box; margin: 0; padding: 0; }
  html, body {
    width: 1200px; height: 1200px; overflow: hidden;
    background: var(--page);
  }
  .canvas { position: relative; width: 1200px; height: 1200px; }
  .label {
    position: absolute; left: 50px; top: 190px;
    width: 1100px; height: 820px;
    background: var(--panel);
    overflow: hidden;
    font-family: "Roboto", Arial, sans-serif;
  }
  .label-texture {
    position: absolute; inset: 0;
    background:
      radial-gradient(ellipse at 60% 40%, var(--panel-light) 0%, transparent 65%),
      linear-gradient(160deg, #333335 0%, var(--panel) 60%, #262628 100%);
  }
  .name-band {
    position: absolute; left: 0; top: 0;
    width: 211px; height: 820px;
    background: var(--pink);
  }
  .product-name {
    position: absolute; left: 105px; top: 400px;
    transform: translate(-50%, -50%) rotate(-90deg);
    font-family: "Roboto Condensed", "Arial Narrow", sans-serif;
    font-weight: 700; font-size: 150px; line-height: 1;
    color: var(--white); white-space: nowrap;
  }
  .category {
    position: absolute; left: 295px; top: 400px;
    transform: translate(-50%, -50%) rotate(-90deg);
    font-family: "Roboto Condensed", "Arial Narrow", sans-serif;
    font-weight: 300; font-size: 66px; line-height: 1;
    color: var(--pink); white-space: nowrap; letter-spacing: 2px;
  }
  .ribbon { position: absolute; left: 0; top: 0; width: 1100px; height: 820px; }
  .ribbon text {
    font-family: "Roboto Condensed", "Arial Narrow", sans-serif;
    font-weight: 700; fill: var(--white);
  }
  .center {
    position: absolute; left: 399px; width: 600px; top: 0; height: 820px;
    text-align: center;
  }
  .center > * { position: absolute; left: 50%; transform: translateX(-50%); white-space: nowrap; }
  .brand {
    top: 215px;
    display: flex; align-items: center; gap: 16px;
    font-weight: 500; font-size: 46px; letter-spacing: 5px;
    color: var(--white);
  }
  .brand-mark { width: 22px; height: 22px; background: var(--white); }
  .flavor-art {
    top: 352px; width: 72px; height: 84px;
    border-radius: 46% 46% 50% 50% / 30% 30% 70% 70%;
    background: linear-gradient(180deg, var(--leaf) 0%, var(--leaf) 14%, var(--berry-light) 22%, var(--berry) 100%);
  }
  .flavor {
    top: 450px; font-weight: 700; font-size: 30px; color: var(--pink-soft);
  }
  .size-pill {
    top: 568px; width: 220px; height: 44px; line-height: 44px; border-radius: 22px;
    background: var(--pink); color: var(--white);
    font-weight: 700; font-size: 22px;
  }
  .slogan {
    top: 668px;
    font-size: 25px; line-height: 40px; color: var(--ink-soft);
    text-transform: uppercase;
  }
</style>
</head>
<body>
<div class="canvas">
  <section class="label">
    <div class="label-texture" role="img" aria-label="Faint repeating triangle pattern on dark grey"></div>
    <div class="name-band"></div>
    <div class="product-name">KIVA LUM</div>
    <div class="category">Food Supplement</div>

    <svg class="ribbon" viewBox="0 0 1100 820" aria-hidden="true">
      <polygon points="800,0 940,0 1100,160 1100,300" fill="#e2385f"/>
      <g transform="translate(1000 132) rotate(45)">
        <text x="0" y="-8" font-size="32" text-anchor="middle">WHEY</text>
        <text x="0" y="28" font-size="38" text-anchor="middle">PROTEIN</text>
      </g>
    </svg>

    <div class="center">
      <div class="brand"><span class="brand-mark"></span>NOVA GRACE</div>
      <div class="flavor-art" role="img" aria-label="Strawberry illustration"></div>
      <div class="flavor">Flavor : Strawberry</div>
      <div class="size-pill">1 fl oz / 30ml</div>
      <p class="slogan">All-in-one premium protein nutritional shake for<br>black women</p>
    </div>
  </section>
</div>
</body>
</html>
```